Design a brochure for bulk SMS service provider

I need a brochure design for bulk SMS provder in South Sudan. The company provides API services for SMS, telephony airtime, bulk SMS and other value added SMS services. Our main product allow people and applications to send and receive SMS locally using our software gateway.
We already have the logo design and would like to see the same colors used in the brochure design. I have attached information data to use in the brochure. much of data is in form of lists. I would prefer a grid layout for list items with each having small icon that relates to information the list item communicates.
I have attached a some images of models to use in the design. such as cover page. you can add more images where you see fit.

Target Market(s)

East Africa Region

Industry/Entity Type

Technology, telecommunication, software

Requirements
Must have
• At least 4 brochure pages, all list items properly layout on grids with icons. I will provide icons for out clients section
Nice to have
• More extra images that convey the message well.
Should not have
• Direct copy of brief large text into one section. e.g Don't copy the use cases section verbatim in to page without design and formatting.

```html
<!DOCTYPE html>
<html lang="en">
<head>
<meta charset="utf-8">
<title>NilaText – Bulk SMS Brochure</title>
<link href="https://fonts.googleapis.com/css2?family=Oswald:wght@500;600;700&family=Roboto:wght@400;500;700&display=swap" rel="stylesheet">
<style>
:root{
  --cyan:#24bdef;
  --cyan-deep:#12a6dc;
  --ink:#111418;
  --text:#2a2d31;
  --white:#ffffff;
  --rule:#c9d3da;
  --backdrop:#dcdfe2;
}
*{box-sizing:border-box;margin:0;padding:0}
html,body{width:1200px;height:1070px;overflow:hidden}
body{background:var(--backdrop);font-family:"Roboto",sans-serif;color:var(--text);position:relative}
.sheet{position:absolute;width:700px;height:494px;background:var(--white);overflow:hidden;box-shadow:0 3px 10px rgba(0,0,0,.22)}
.sheet--outside{left:40px;top:28px}
.sheet--inside{left:460px;top:546px}
.panel{position:absolute;top:0;height:100%}
.panel--blue{background:var(--cyan);color:var(--white)}
.panel--white{background:var(--white)}
.panel--soft{background:linear-gradient(90deg,#e9eef1 0,#fbfcfd 14px,#fff 40px)}

/* icons */
.ico{position:absolute;width:26px;height:26px;border-radius:50%;display:grid;place-items:center}
.ico svg{width:14px;height:14px;fill:none;stroke:currentColor;stroke-width:1.7;stroke-linecap:round;stroke-linejoin:round}
.ico--on-blue{background:var(--cyan);color:var(--white);border:1.5px solid var(--white);box-shadow:0 0 0 2px var(--cyan),0 0 0 3px var(--white)}
.ico--on-white{background:var(--cyan);color:var(--white);box-shadow:0 0 0 2px var(--white),0 0 0 3.2px var(--cyan)}
.rail{position:absolute;width:1.5px}
.rail--white{background:var(--white)}
.rail--cyan{background:var(--cyan)}

/* use-case lists */
.case{position:absolute}
.case__title{font-weight:700;font-size:9px;line-height:11px;margin-bottom:2px;letter-spacing:.1px}
.case__item{display:flex;font-size:7.3px;line-height:9.4px;text-align:justify;margin-bottom:4px}
.case__num{flex:0 0 11px;font-weight:500}
.case__text{flex:1}

/* headings */
.section-title{position:absolute;font-family:"Oswald",sans-serif;font-weight:600;font-size:15px;line-height:18px;letter-spacing:.2px}
.section-title--ink{color:var(--ink)}
.section-title--white{color:var(--white)}
.section-rule{position:absolute;height:1px}

/* cover */
.cover-band{position:absolute;left:350px;top:0;width:91px;height:100%;background:var(--cyan)}
.brand{position:absolute;left:456px;top:36px;display:flex;align-items:center;gap:8px}
.brand__dot{width:30px;height:30px;border-radius:50%;background:var(--cyan)}
.brand__name{font-family:"Roboto",sans-serif;font-weight:700;font-size:34px;line-height:36px;color:var(--ink);letter-spacing:-.5px}
.photo{position:absolute;border:3px solid var(--white)}
.photo--cover{left:378px;top:98px;width:322px;height:284px;background:linear-gradient(135deg,#f2a94a 0%,#d9793a 30%,#6c6f7d 62%,#2f4d6a 100%)}
.photo--team{left:19px;top:20px;width:314px;height:205px;background:linear-gradient(180deg,#eceae6 0%,#dedbd5 45%,#9ca9b8 75%,#3d4b5e 100%)}
.headline{position:absolute;left:449px;top:405px;font-family:"Oswald",sans-serif;font-weight:700;font-size:24.5px;line-height:29px;letter-spacing:-.2px;text-transform:uppercase}
.headline__dark{color:var(--ink);display:block}
.headline__blue{color:var(--cyan);display:block}

/* clients */
.clients{position:absolute;left:185px;top:20px;width:151px;height:159px;border:1px solid var(--rule);border-radius:4px}
.clients__title{position:absolute;top:-7px;left:50%;transform:translateX(-50%);background:var(--white);padding:0 5px;font-family:"Oswald",sans-serif;font-weight:600;font-size:9.5px;line-height:13px;color:var(--ink);white-space:nowrap}
.clients__list{position:absolute;top:10px;left:0;right:0;display:flex;flex-direction:column;align-items:center;gap:6px}
.client{font-family:"Roboto",sans-serif;font-weight:500;font-size:12px;line-height:14px;color:var(--cyan-deep)}
.client--dark{color:#2c3238}
.client--navy{color:#2f58a6;font-size:9.5px}
.client-badge{width:44px;height:44px;border-radius:50%;background:#d9dee3}
.device{position:absolute;left:212px;top:189px;width:94px;height:190px;border-radius:13px;background:linear-gradient(180deg,#2a2d33 0%,#bcc6d6 12%,#d5dcea 60%,#b9c3d3 88%,#2a2d33 100%)}

/* contact */
.contact{position:absolute;left:186px;top:387px;width:150px;height:92px;background:#050506;padding:8px 8px 0 8px;color:var(--white)}
.contact__title{font-family:"Oswald",sans-serif;font-weight:600;font-size:10px;line-height:12px;color:var(--cyan);margin-bottom:3px}
.contact__row{display:flex;gap:4px;font-size:6.6px;line-height:8.4px;margin-bottom:4px}
.contact__row svg{flex:0 0 7px;width:7px;height:7px;margin-top:1px}
.contact__row b{font-weight:700}

/* about */
.about{position:absolute;left:18px;top:262px;width:152px;font-size:7.9px;line-height:11.3px;text-align:justify;color:var(--white)}
.about p+p{margin-top:10px}

/* solution & feature rows */
.rows{position:absolute;display:flex;flex-direction:column}
.row{position:relative}
.row__text{font-size:7.3px;line-height:9.4px;text-align:justify;color:var(--text)}
.row__text b{font-weight:700;color:var(--ink);font-size:8px}
.panel--blue .row__text{color:var(--white)}
</style>
</head>
<body>

<svg width="0" height="0" style="position:absolute" aria-hidden="true">
  <symbol id="i-health" viewBox="0 0 24 24"><path d="M10 4h4v6h6v4h-6v6h-4v-6H4v-4h6z"/></symbol>
  <symbol id="i-dish" viewBox="0 0 24 24"><circle cx="12" cy="12" r="7"/><path d="M5 5l14 14"/></symbol>
  <symbol id="i-book" viewBox="0 0 24 24"><path d="M4 6h7v13H4zM13 6h7v13h-7z"/></symbol>
  <symbol id="i-mail" viewBox="0 0 24 24"><rect x="3" y="6" width="18" height="12" rx="1"/><path d="M3 7l9 6 9-6"/></symbol>
  <symbol id="i-inbox" viewBox="0 0 24 24"><path d="M4 13l3-7h10l3 7v5H4z"/><path d="M4 13h5l1 2h4l1-2h5"/></symbol>
  <symbol id="i-refresh" viewBox="0 0 24 24"><path d="M19 8a7 7 0 0 0-13 1M5 16a7 7 0 0 0 13-1"/><path d="M19 4v4h-4M5 20v-4h4"/></symbol>
  <symbol id="i-chat" viewBox="0 0 24 24"><path d="M4 5h16v10H9l-4 4v-4H4z"/></symbol>
  <symbol id="i-poll" viewBox="0 0 24 24"><path d="M6 18v-5M12 18V7M18 18v-8M4 20h16"/></symbol>
  <symbol id="i-coin" viewBox="0 0 24 24"><ellipse cx="12" cy="7" rx="6" ry="2.5"/><path d="M6 7v10c0 1.4 2.7 2.5 6 2.5s6-1.1 6-2.5V7M6 12c0 1.4 2.7 2.5 6 2.5s6-1.1 6-2.5"/></symbol>
  <symbol id="i-clip" viewBox="0 0 24 24"><rect x="6" y="5" width="12" height="15" rx="1"/><path d="M9 4h6v3H9zM9 11h6M9 15h4"/></symbol>
  <symbol id="i-phone" viewBox="0 0 24 24"><rect x="7" y="3" width="10" height="18" rx="2"/><path d="M11 18h2"/></symbol>
  <symbol id="i-code" viewBox="0 0 24 24"><path d="M9 7l-5 5 5 5M15 7l5 5-5 5"/></symbol>
  <symbol id="i-mega" viewBox="0 0 24 24"><path d="M4 10v4h3l9 4V6l-9 4z"/><path d="M19 10v4"/></symbol>
  <symbol id="i-bank" viewBox="0 0 24 24"><path d="M3 10l9-5 9 5zM5 10v7M9.7 10v7M14.3 10v7M19 10v7M3 19h18"/></symbol>
  <symbol id="i-heart" viewBox="0 0 24 24"><path d="M12 19s-7-4.4-7-9.5A3.8 3.8 0 0 1 12 7a3.8 3.8 0 0 1 7 2.5C19 14.6 12 19 12 19z"/></symbol>
  <symbol id="i-pin" viewBox="0 0 24 24"><path d="M12 21s-6-6.2-6-11a6 6 0 0 1 12 0c0 4.8-6 11-6 11z"/><circle cx="12" cy="10" r="2"/></symbol>
  <symbol id="i-tel" viewBox="0 0 24 24"><path d="M5 4h4l2 5-2.5 1.5a11 11 0 0 0 5 5L15 13l5 2v4a1 1 0 0 1-1 1A16 16 0 0 1 4 5a1 1 0 0 1 1-1z"/></symbol>
</svg>

<!-- OUTSIDE SPREAD -->
<section class="sheet sheet--outside" aria-label="Brochure outside">

  <div class="panel panel--blue" style="left:0;width:178px">
    <div class="rail rail--white" style="left:31px;top:30px;height:340px"></div>

    <div class="case" style="left:14px;top:16px;width:154px">
      <span class="ico ico--on-blue" style="left:4px;top:2px"><svg><use href="#i-health"/></svg></span>
      <div style="margin-left:40px">
        <p class="case__title">HEALTHCARE -</p>
        <p class="case__item"><span class="case__num">1)</span><span class="case__text">Send automated confirmations &amp; reminders for doctor appointments, medical tests</span></p>
        <p class="case__item"><span class="case__num">2)</span><span class="case__text">Issue mobile visitor passes to patients' visitors &amp; limit access to the patient rooms using SMS</span></p>
        <p class="case__item"><span class="case__num">3)</span><span class="case__text">Allow patients to seek appointments by texting the time slot to the hospital's SMS inbox setup using short code or long code services</span></p>
        <p class="case__item"><span class="case__num">4)</span><span class="case__text">Allow patients to request emergency assistance by texting in a pre-defined keyword to your SMS inbox.</span></p>
      </div>
    </div>

    <div class="case" style="left:14px;top:224px;width:154px">
      <span class="ico ico--on-blue" style="left:4px;top:2px"><svg><use href="#i-dish"/></svg></span>
      <div style="margin-left:40px">
        <p class="case__title">Restaurant &amp; takeways –</p>
        <p class="case__item"><span class="case__num">1)</span><span class="case__text">Encourage restaurant visitors to text into your SMS long-codes/shortcodes to receive special invites and offers. Grow your opt-in database.</span></p>
        <p class="case__item"><span class="case__num">2)</span><span class="case__text">Entice customers with limited time discount vouchers for lean hours sent via SMS.</span></p>
      </div>
    </div>

    <div class="case" style="left:14px;top:343px;width:154px">
      <span class="ico ico--on-blue" style="left:4px;top:2px"><svg><use href="#i-book"/></svg></span>
      <div style="margin-left:40px">
        <p class="case__title">Education –</p>
        <p class="case__item"><span class="case__num">1)</span><span class="case__text">Use bulk SMS to send information about exam schedules, reading material, and meeting invites to students, parents and staff.</span></p>
        <p class="case__item"><span class="case__num">2)</span><span class="case__text">Allow student to query exams results using two way SMS</span></p>
        <p class="case__item"><span class="case__num">3)</span><span class="case__text">Get real time and quick feedback about students, teachers, courses &amp; facilities using SMS surveys.</span></p>
      </div>
    </div>
  </div>

  <div class="panel panel--white" style="left:178px;width:172px"></div>

  <div class="clients">
    <p class="clients__title">OUR CLIENTS</p>
    <div class="clients__list">
      <span class="client">Kidwell Fund</span>
      <span class="client client--dark">SurveyLine</span>
      <span class="client client--navy">HARBOR HEALTH GROUP</span>
      <span class="client-badge" aria-hidden="true"></span>
      <span class="client">ShopNile</span>
    </div>
  </div>

  <div class="device" role="img" aria-label="Smartphone showing an SMS conversation"></div>

  <div class="contact">
    <p class="contact__title">CONTACT US</p>
    <p class="contact__row"><svg viewBox="0 0 24 24" fill="none" stroke="#24bdef" stroke-width="2.4"><use href="#i-pin"/></svg><span>Kesto Plaza office No. 7, Central Equatoria State, Juba – South Sudan</span></p>
    <p class="contact__row"><svg viewBox="0 0 24 24" fill="none" stroke="#24bdef" stroke-width="2.4"><use href="#i-tel"/></svg><span>211 900 555 014</span></p>
    <p class="contact__row"><svg viewBox="0 0 24 24" fill="none" stroke="#24bdef" stroke-width="2.4"><use href="#i-mail"/></svg><span><b>Sales:</b> sales@nilatext.com</span></p>
    <p class="contact__row"><svg viewBox="0 0 24 24" fill="none" stroke="#24bdef" stroke-width="2.4"><use href="#i-mail"/></svg><span><b>Support:</b> info@nilatext.com</span></p>
  </div>

  <div class="panel panel--white" style="left:350px;width:350px"></div>
  <div class="cover-band"></div>
  <div class="brand"><span class="brand__dot" aria-hidden="true"></span><span class="brand__name">NilaText</span></div>
  <div class="photo photo--cover" role="img" aria-label="Group of young friends laughing while looking at their mobile phones"></div>
  <h1 class="headline"><span class="headline__dark">NilaText is a bulk SMS</span><span class="headline__blue">provider in South Sudan</span></h1>
</section>

<!-- INSIDE SPREAD -->
<section class="sheet sheet--inside" aria-label="Brochure inside">

  <div class="panel panel--blue" style="left:0;width:185px"></div>
  <div class="panel panel--white" style="left:185px;width:165px"></div>
  <div class="panel panel--soft" style="left:350px;width:175px"></div>
  <div class="panel panel--blue" style="left:525px;width:175px"></div>

  <div class="photo photo--team" role="img" aria-label="Four young people leaning on a wall using phones, with colourful app and messaging icons above them"></div>

  <h2 class="section-title section-title--white" style="left:18px;top:234px">ABOUT US</h2>
  <div class="section-rule" style="left:18px;top:255px;width:152px;background:var(--white)"></div>
  <div class="about">
    <p>NilaText is a bulk SMS provider in South Sudan having 5+ years experience in providing multiroutes message solutions to promote your business. Increase sales and customer satisfaction with smarter SMS campaigns, instant OTPs, notifications, two-way interactions and other innovative bulk SMS services.</p>
    <p>Our focus is to facilitate SMS routing and delivery and as well as help businesses hop through myriad of regulations put forth by authorities in South Sudan. Using our many partner telecommunication providers, we are able to push your message on a predictable route and be sure of delivery.</p>
  </div>

  <h2 class="section-title section-title--ink" style="left:202px;top:244px">OUR SOLUTIONS</h2>
  <div class="rail rail--cyan" style="left:213px;top:275px;height:190px"></div>
  <div class="rows" style="left:201px;top:264px;width:131px;gap:8px">
    <div class="row"><span class="ico ico--on-white" style="left:0;top:2px"><svg><use href="#i-phone"/></svg></span><p class="row__text" style="margin-left:33px"><b>SMS aggregation –</b> Send and receive SMS easily from any network in South Sudan</p></div>
    <div class="row"><span class="ico ico--on-white" style="left:0;top:0"><svg><use href="#i-chat"/></svg></span><p class="row__text" style="margin-left:33px"><b>Bulk SMS –</b> Send to multiple people at the same time using one request.</p></div>
    <div class="row"><span class="ico ico--on-white" style="left:0;top:4px"><svg><use href="#i-coin"/></svg></span><p class="row__text" style="margin-left:33px"><b>Airtime –</b> Provide airtime distribution services to mobile phone users in South Sudan</p></div>
    <div class="row"><span class="ico ico--on-white" style="left:0;top:0"><svg><use href="#i-phone"/></svg></span><p class="row__text" style="margin-left:33px"><b>USSD –</b> Build interactive applications using our USSD API</p></div>
    <div class="row"><span class="ico ico--on-white" style="left:0;top:2px"><svg><use href="#i-code"/></svg></span><p class="row__text" style="margin-left:33px"><b>Short codes –</b> Offer short numbers to send &amp; receive SMS in South Sudan.</p></div>
  </div>

  <h2 class="section-title section-title--ink" style="left:368px;top:18px">OUR FEATURES</h2>
  <div class="rail rail--cyan" style="left:385px;top:52px;height:410px"></div>
  <div class="rows" style="left:373px;top:40px;width:143px;gap:9px">
    <div class="row"><span class="ico ico--on-white" style="left:0;top:2px"><svg><use href="#i-mail"/></svg></span><p class="row__text" style="margin-left:37px"><b>Send SMS -</b> Easily Send SMS with different methods (web, http, smpp)</p></div>
    <div class="row"><span class="ico ico--on-white" style="left:0;top:8px"><svg><use href="#i-inbox"/></svg></span><p class="row__text" style="margin-left:37px"><b>Receive SMS -</b> Easily receive SMS in South Sudan using a combination of catchy keywords, short codes and long codes provided by NilaText</p></div>
    <div class="row"><span class="ico ico--on-white" style="left:0;top:6px"><svg><use href="#i-refresh"/></svg></span><p class="row__text" style="margin-left:37px"><b>Auto Responders –</b> Easily compose an automated SMS response that is sent to every customer who texts to your short code</p></div>
    <div class="row"><span class="ico ico--on-white" style="left:0;top:10px"><svg><use href="#i-chat"/></svg></span><p class="row__text" style="margin-left:37px"><b>Two Way SMS –</b> You can request short codes, long codes or even use one of our shared short codes to receive and send messages to your customer. Create unlimited keywords on these codes too.</p></div>
    <div class="row"><span class="ico ico--on-white" style="left:0;top:4px"><svg><use href="#i-poll"/></svg></span><p class="row__text" style="margin-left:37px"><b>SMS Polls -</b> Conduct polls, interact with customers and build your database by receiving SMS</p></div>
    <div class="row"><span class="ico ico--on-white" style="left:0;top:4px"><svg><use href="#i-coin"/></svg></span><p class="row__text" style="margin-left:37px"><b>Airtime –</b> Send airtime easily to your customers in South Sudan using our simple REST API feature.</p></div>
    <div class="row"><span class="ico ico--on-white" style="left:0;top:4px"><svg><use href="#i-clip"/></svg></span><p class="row__text" style="margin-left:37px"><b>Delivery Reports -</b> Know at any given time the status of outgoing SMS sent using any of our various methods.</p></div>
    <div class="row"><span class="ico ico--on-white" style="left:0;top:2px"><svg><use href="#i-chat"/></svg></span><p class="row__text" style="margin-left:37px"><b>USSD –</b> Easily build interactive aplications on top of USSD framework</p></div>
  </div>

  <h2 class="section-title section-title--white" style="left:532px;top:18px">USE CASES</h2>
  <div class="section-rule" style="left:532px;top:39px;width:148px;background:var(--white)"></div>
  <div class="rail rail--white" style="left:551px;top:60px;height:412px"></div>

  <div class="case" style="left:539px;top:44px;width:143px">
    <span class="ico ico--on-blue" style="left:0;top:8px"><svg><use href="#i-mega"/></svg></span>
    <div style="margin-left:37px">
      <p class="case__title">MARKETING AND ADS –</p>
      <p class="case__item"><span class="case__text">Easily send promotional messages using our platform. Whether it is personalizing millions of texts via multiple merge fields, sending regional language texts, sharing images and files via SMS, staggering large pushes in batches, it is all incredibly easy with NilaText</span></p>
    </div>
  </div>

  <div class="case" style="left:539px;top:172px;width:143px">
    <span class="ico ico--on-blue" style="left:0;top:6px"><svg><use href="#i-bank"/></svg></span>
    <div style="margin-left:37px">
      <p class="case__title">BANKING &amp; FINANCIAL SERVICES -</p>
      <p class="case__item"><span class="case__num">1)</span><span class="case__text">Send transnational alerts</span></p>
      <p class="case__item"><span class="case__num">2)</span><span class="case__text">Send SMS campaign your customers love. Our platform provide powerful personalization features</span></p>
      <p class="case__item"><span class="case__num">3)</span><span class="case__text">Control queue using SMS supported applications.</span></p>
    </div>
  </div>

  <div class="case" style="left:539px;top:295px;width:143px">
    <span class="ico ico--on-blue" style="left:0;top:6px"><svg><use href="#i-heart"/></svg></span>
    <div style="margin-left:37px">
      <p class="case__title">NGO –</p>
      <p class="case__item"><span class="case__num">1)</span><span class="case__text">No need to hand out pamphlets or send them via post. Easily create &amp; send memorable promotional SMS campaigns</span></p>
      <p class="case__item"><span class="case__num">2)</span><span class="case__text">Keep your donors regularly updated with reports and news of activities through a simple SMS that includes web links to relevant information</span></p>
      <p class="case__item"><span class="case__num">3)</span><span class="case__text">Remote areas communication using SMS. Build apps on top of our gateway that can support your on site team.</span></p>
    </div>
  </div>
</section>

</body>
</html>
```